Marlow Naturopathics business card design

Using the marlow logo designed, we would like that incorporated into a business card. A colour scheme which works with the logo and lists the following business details:

Dennis Marlow - Naturopath
Level 1, 58 Torvane Street
Wollongong NSW
(02) 4391 7084
www.dennismarlowhealth-example.com

We would also like space on the back of the card for next appointment times.

Target Market(s)

Anyone looking to improve their health

Industry/Entity Type

Business

Requirements
Must have
• Marlow Naturopathics logo, business details.
Nice to have
• Good colour schemes, attractive, eye-catching features that are easy to read.

```html
<!DOCTYPE html>
<html lang="en">
<head>
<meta charset="utf-8">
<title>Marlow Naturopathics – Business Card</title>
<link rel="stylesheet" href="https://fonts.googleapis.com/css2?family=Questrial&display=swap">
<style>
  :root {
    --page-bg: #e7e5e2;
    --card-light: #ffffff;
    --card-mid: #eeeeee;
    --leaf-green: #2f8a2b;
    --leaf-bright: #56c23a;
    --leaf-deep: #2c6e1f;
    --band-rule: #6d6d6d;
    --ink: #3a3a3a;
    --ink-soft: #555555;
    --line: #9bb58e;
    --ghost: #d6d6d6;
  }
  * { box-sizing: border-box; margin: 0; padding: 0; }
  html, body { width: 1200px; height: 900px; overflow: hidden; }
  body {
    background: var(--page-bg);
    font-family: "Questrial", "Century Gothic", sans-serif;
    position: relative;
  }
  .card {
    position: absolute;
    left: 250px;
    width: 700px;
    height: 400px;
    border-radius: 26px;
    overflow: hidden;
    background: linear-gradient(180deg, var(--card-light) 0%, var(--card-mid) 100%);
    box-shadow: 0 6px 18px rgba(0,0,0,0.18);
  }
  .card--back { top: 40px; }
  .card--front { top: 460px; }

  /* Back: appointment side */
  .photo-band {
    position: absolute;
    left: 0; right: 0;
    top: 34px;
    height: 196px;
    border-top: 4px solid var(--band-rule);
    border-bottom: 4px solid var(--band-rule);
  }
  .photo-band__image {
    position: absolute; inset: 0;
    background: radial-gradient(ellipse at 70% 35%, var(--leaf-bright) 0%, var(--leaf-green) 55%, var(--leaf-deep) 100%);
  }
  .photo-band__title {
    position: absolute;
    left: 30px; bottom: 18px;
    color: #ffffff;
    font-size: 22px;
    letter-spacing: 0.5px;
    white-space: nowrap;
  }
  .appointment {
    position: absolute;
    left: 380px; top: 180px;
    width: 290px; height: 150px;
    background: rgba(240,240,240,0.95);
    border: 1px solid #d8d8d8;
    border-radius: 8px;
    padding: 14px 20px;
  }
  .appointment__heading {
    font-size: 16px;
    color: var(--ink);
    margin-bottom: 10px;
  }
  .appointment__row {
    display: flex;
    align-items: flex-end;
    height: 32px;
    font-size: 10px;
    text-transform: uppercase;
    color: var(--ink-soft);
  }
  .appointment__row span { margin-right: 8px; }
  .appointment__line {
    flex: 1;
    border-bottom: 1px solid var(--line);
    margin-bottom: 2px;
  }

  /* Front: contact side */
  .ghost-image { position: absolute; opacity: 0.55; }
  .ghost-image--top {
    right: 0; top: 0;
    width: 360px; height: 130px;
    background: radial-gradient(ellipse at 50% 60%, var(--ghost) 0%, rgba(230,230,230,0) 75%);
  }
  .ghost-image--bottom {
    left: 0; bottom: 0;
    width: 320px; height: 100px;
    background: radial-gradient(ellipse at 40% 60%, var(--ghost) 0%, rgba(230,230,230,0) 75%);
  }
  .identity {
    position: absolute;
    left: 70px; top: 176px;
  }
  .identity__name {
    font-size: 34px;
    font-weight: 400;
    color: var(--ink);
    letter-spacing: 0.5px;
    white-space: nowrap;
  }
  .identity__role {
    font-size: 18px;
    color: var(--leaf-green);
    margin-top: 6px;
  }
  .contact {
    position: absolute;
    left: 350px; top: 166px;
    list-style: none;
    color: var(--leaf-green);
    font-size: 15px;
  }
  .contact__item {
    display: flex;
    align-items: flex-start;
    line-height: 28px;
    white-space: nowrap;
  }
  .contact__icon {
    width: 15px; height: 15px;
    margin: 6px 16px 0 0;
    flex-shrink: 0;
    fill: var(--ink);
  }
</style>
</head>
<body>

  <section class="card card--back" aria-label="Card back: appointment reminder">
    <div class="photo-band">
      <div class="photo-band__image" role="img" aria-label="Photograph of unfurling fern fronds on a green background"></div>
      <p class="photo-band__title">Dennis Marlow Naturopath</p>
    </div>
    <div class="appointment">
      <p class="appointment__heading">Your next appointment:</p>
      <div class="appointment__row"><span>Name:</span><div class="appointment__line"></div></div>
      <div class="appointment__row"><span>Date:</span><div class="appointment__line"></div></div>
      <div class="appointment__row"><span>Time:</span><div class="appointment__line"></div></div>
    </div>
  </section>

  <section class="card card--front" aria-label="Card front: contact details">
    <div class="ghost-image ghost-image--top" role="img" aria-label="Faint image of fern fronds"></div>
    <div class="ghost-image ghost-image--bottom" role="img" aria-label="Faint image of fern fronds"></div>

    <div class="identity">
      <h1 class="identity__name">Dennis Marlow</h1>
      <p class="identity__role">Naturopath</p>
    </div>

    <ul class="contact">
      <li class="contact__item">
        <svg class="contact__icon" viewBox="0 0 16 16" aria-hidden="true">
          <path d="M4 1.5 6.2 4.5 5 6c.8 1.8 2.2 3.2 4 4l1.5-1.2 3 2.2-1.2 2.4C7.4 13.5 2.5 8.6 1.6 3.1Z"/>
        </svg>
        <span>(02) 4391 7084</span>
      </li>
      <li class="contact__item">
        <svg class="contact__icon" viewBox="0 0 16 16" aria-hidden="true">
          <path d="M8 1.5 15 8h-2v6h-3.5v-4h-3v4H3V8H1Z"/>
        </svg>
        <span>www.dennismarlowhealth-example.com</span>
      </li>
      <li class="contact__item">
        <svg class="contact__icon" viewBox="0 0 16 16" aria-hidden="true">
          <path d="M8 0.5a5 5 0 0 0-5 5c0 3.8 5 10 5 10s5-6.2 5-10a5 5 0 0 0-5-5Zm0 7a2 2 0 1 1 0-4 2 2 0 0 1 0 4Z"/>
        </svg>
        <span>Level 1, 58 Torvane Street<br>Wollongong NSW</span>
      </li>
    </ul>
  </section>

</body>
</html>
```